Pine Hollow Camp Brochure Design - TRI FOLD - See text examples added

Tri- Fold Brochure designed for Remote Alaskan Wilderness Fly-in lodge.We will provide several pictures. We want activities, directions, lodge rules, history, etc... We have provided our logo. Will work on adding text.
Looking for a professional, fun, adventurous feel.
Guests must fly in to the lodge. We are completely surrounded by wilderness. 33 miles from the nearest road. Take a 30 min flight seeing trip over mountains, glaciers, rivers and wildlife with Skyhop Tours to our private airstrip. Canoe in Otter Pond. See the Moose, Caribou, Bears, Lynx, wolves, and various birds. Go gold panning in the creeks.
Accommodations include your own private cabin with private bathroom. Access to the main lodge lounge and dining rooms, wood fired sauna, covered fire pit, and use of our canoe, life jackets, and rubber boots. Meals available. Wifi in main lodge. Movies in Theater.

Target Market(s)

Adventure, photographers, hikers, mountaineers, travelers

Industry/Entity Type

Tourism

Requirements
Must have
• Logo and pictures, information - Tri-Fold
Nice to have
• High quality attractive design with logo and information
Should not have
• Cartoony feel

```html
<!DOCTYPE html>
<html lang="en">
<head>
<meta charset="utf-8">
<title>Pine Hollow Camp – Tri-Fold Brochure</title>
<link href="https://fonts.googleapis.com/css2?family=Oswald:wght@400;500&family=Open+Sans:wght@400;600&family=Kaushan+Script&family=Rye&display=swap" rel="stylesheet">
<style>
:root{
  --page:#e4e4e4;
  --orange:#e8581c;
  --orange-lt:#f07a3a;
  --wood-1:#5a3a2b;
  --wood-2:#3e2519;
  --wood-3:#6b4634;
  --navy-1:#1f2a36;
  --navy-2:#141c26;
  --ink:#2b2b2b;
  --cream:#ffffff;
  --sky:#dbe9f1;
}
*{box-sizing:border-box;margin:0;padding:0}
html,body{width:780px;height:1200px;overflow:hidden;background:var(--page)}
body{position:relative;font-family:'Open Sans',sans-serif;color:var(--cream)}
.sheet{position:absolute;left:40px;width:700px;height:543px;overflow:hidden;background:#fff}
.sheet--outer{top:30px}
.sheet--inner{top:627px}
.panel{position:absolute;top:0;height:543px;overflow:hidden}
.wood{background:linear-gradient(100deg,var(--wood-3),var(--wood-1) 45%,var(--wood-2))}
.navy{background:linear-gradient(180deg,var(--navy-1),var(--navy-2))}
.photo{position:absolute;left:0;top:0;width:100%}
.curve{position:absolute;left:0;width:100%}
.ring{position:absolute;border-radius:50%;border:4px solid var(--orange);box-shadow:0 0 0 2px rgba(232,88,28,.35)}
.head{font-family:'Oswald',sans-serif;font-weight:400;text-transform:uppercase;letter-spacing:.2px}
.script{font-family:'Kaushan Script',cursive;color:var(--orange)}
.body{font-size:9px;line-height:1.42;text-align:justify}
.band{position:absolute;background:var(--orange);color:#fff;font-family:'Oswald',sans-serif;text-transform:uppercase;display:flex;align-items:center;justify-content:center;gap:5px;
  clip-path:polygon(2% 8%,30% 0,70% 6%,99% 0,100% 45%,97% 100%,60% 92%,25% 100%,0 94%,1% 50%)}
.band svg{width:12px;height:12px}
.web{position:absolute;font-weight:600;font-size:11px;text-align:center}
.brandmark{position:absolute;display:flex;flex-direction:column;align-items:center;justify-content:center;text-align:center;font-family:'Oswald',sans-serif;font-weight:500;text-transform:uppercase;line-height:1.05}
.brandmark__dot{width:14px;height:14px;border-radius:50%;background:currentColor;margin-bottom:6px}
.list{list-style:none;font-size:9.5px;line-height:1.85}
.list li{display:flex;align-items:center;gap:6px}
.list li::before{content:"";width:9px;height:9px;border-radius:50%;background:var(--orange);flex:none}
.thumb{position:absolute;border:3px solid #fff;box-shadow:0 1px 3px rgba(0,0,0,.3)}
</style>
</head>
<body>

<!-- OUTER SHEET -->
<section class="sheet sheet--outer">

  <!-- Panel 1: remote property -->
  <div class="panel panel--remote wood" style="left:0;width:233px">
    <div class="photo" role="img" aria-label="Log cabin with moose antlers above the porch, trees and mountains behind" style="height:280px;background:linear-gradient(170deg,#c9d6dc,#7c8a6d 35%,#5b4433 70%,#3b2a20)"></div>
    <svg class="curve" style="top:262px" viewBox="0 0 233 40" height="40" preserveAspectRatio="none"><path d="M0 30 Q120 0 233 8 L233 40 L0 40Z" fill="var(--wood-1)"/><path d="M0 30 Q120 0 233 8" stroke="#fff" stroke-width="3" fill="none"/></svg>
    <div class="ring" role="img" aria-label="Small plane parked on a grass airstrip" style="left:16px;top:205px;width:104px;height:104px;background:radial-gradient(#aab9c4,#6f7d66)"></div>
    <div class="ring" role="img" aria-label="Dall sheep on a rocky slope" style="left:120px;top:222px;width:90px;height:90px;background:radial-gradient(#9a9385,#5a5045)"></div>
    <div class="head" style="position:absolute;left:16px;top:326px;font-size:15px;line-height:1.3">Remote Property!!<br>There are no roads here!!</div>
    <div class="script" style="position:absolute;left:16px;top:366px;font-size:15px">You Must Fly!!</div>
    <p class="body" style="position:absolute;left:16px;top:393px;width:202px">From Healy airport, Skyhop Tours will take you on a 30 min scenic tour of mountains, rivers, glaciers and wildlife.</p>
    <p class="body" style="position:absolute;left:16px;top:440px;width:202px">Upon arrival at Pine Hollow Camp, our staff will greet you and give you a tour of the property including over 25 historic buildings. Guests will be shown to their private cabins with private baths. Rates are based per cabin.</p>
    <div class="band" style="left:30px;top:509px;width:178px;height:22px;font-family:'Open Sans',sans-serif;font-weight:600;font-size:10.5px;text-transform:none">www.pinehollowcamp.com</div>
  </div>

  <!-- Panel 2: welcome -->
  <div class="panel panel--welcome navy" style="left:233px;width:233px">
    <div class="photo" role="img" aria-label="Autumn valley with a lake, spruce trees and distant mountains at dusk" style="height:270px;background:linear-gradient(180deg,#4c5a6e,#8a94a0 25%,#9e7b45 55%,#3a3a2c 85%)"></div>
    <svg class="curve" style="top:240px" viewBox="0 0 233 40" height="40" preserveAspectRatio="none"><path d="M0 10 Q110 40 233 12 L233 40 L0 40Z" fill="var(--navy-1)"/></svg>
    <div class="brandmark" style="left:63px;top:136px;width:108px;height:108px;border-radius:50%;background:var(--navy-2);color:#fff;font-size:16px">Pine Hollow<br>Camp</div>
    <div class="script" style="position:absolute;left:0;width:233px;top:294px;text-align:center;font-size:15px">This Is The Real Alaska!</div>
    <div class="head" style="position:absolute;left:0;width:233px;top:318px;text-align:center;font-size:12px">Book your trip now</div>
    <div class="band" style="left:36px;top:338px;width:160px;height:20px;font-size:11px">Call us today
      <svg viewBox="0 0 12 12"><circle cx="6" cy="6" r="5.2" fill="none" stroke="#fff" stroke-width="1"/><path d="M4 3.2l1 1.2-.6.8c.3.8.9 1.4 1.6 1.7l.8-.6 1.2 1-.6 1.1c-2-.2-3.7-2-3.9-3.9z" fill="#fff"/></svg>
      907-555-0142</div>
    <div style="position:absolute;left:0;width:233px;top:361px;text-align:center;font-size:10px">stay@pinehollowcamp.com</div>
    <div class="head" style="position:absolute;left:0;width:233px;top:394px;text-align:center;font-size:10.5px">Welcome to Pine Hollow Camp est. 1898!</div>
    <p class="body" style="position:absolute;left:16px;top:422px;width:202px">Guests will be shown to their private cabins with private baths. Rates are based per cabin. Cabins can have a single queen, a queen and single, or two singles and a queen.</p>
    <p class="body" style="position:absolute;left:16px;top:476px;width:202px">Spend your time hiking one of several marked trails, climbing Mt. Anderson, use our canoe on Otter Pond, gold pan the creeks, and much more!</p>
    <div class="web" style="left:0;width:233px;top:516px;color:var(--orange)">www.pinehollowcamp.com</div>
  </div>

  <!-- Panel 3: cover -->
  <div class="panel panel--cover wood" style="left:466px;width:234px">
    <div style="position:absolute;left:0;top:0;width:234px;height:140px;background:#fff"></div>
    <div class="photo" role="img" aria-label="Family smiling in a canoe on a mountain lake" style="top:120px;height:272px;background:linear-gradient(180deg,#eef2f4,#8fa6a8 22%,#3e5a4f 45%,#6f8a86 70%,#4c6b73)"></div>
    <div class="brandmark" style="left:55px;top:10px;width:124px;height:110px;color:var(--navy-1);font-size:19px"><span class="brandmark__dot"></span>Pine Hollow<br>Camp</div>
    <svg class="curve" style="top:360px" viewBox="0 0 234 40" height="40" preserveAspectRatio="none"><path d="M0 30 Q120 0 234 18 L234 40 L0 40Z" fill="var(--wood-1)"/><path d="M0 30 Q120 0 234 18" stroke="#fff" stroke-width="3" fill="none"/></svg>
    <div style="position:absolute;left:0;width:234px;top:418px;text-align:center;font-family:'Rye',serif;font-size:19px;line-height:1.55;color:#f3ece6">Remote Alaskan<br>Wilderness</div>
    <div class="band" style="left:16px;top:486px;width:204px;height:24px;font-size:14px">Call us today
      <svg viewBox="0 0 12 12"><circle cx="6" cy="6" r="5.2" fill="none" stroke="#fff" stroke-width="1"/><path d="M4 3.2l1 1.2-.6.8c.3.8.9 1.4 1.6 1.7l.8-.6 1.2 1-.6 1.1c-2-.2-3.7-2-3.9-3.9z" fill="#fff"/></svg>
      907-555-0142</div>
    <div class="web" style="left:0;width:234px;top:517px;letter-spacing:.8px">www.pinehollowcamp.com</div>
  </div>
</section>

<!-- INNER SHEET -->
<section class="sheet sheet--inner">

  <!-- Left panel: intro -->
  <div class="panel panel--intro" style="left:0;width:233px;background:linear-gradient(180deg,#fff 55%,var(--sky));color:var(--ink)">
    <div class="head" style="position:absolute;left:16px;top:28px;font-size:11px;color:#4a2a1c">Welcome to Pine Hollow Camp est. 1898!</div>
    <div class="script" style="position:absolute;left:16px;top:44px;font-size:13px">This Is The Real Alaska!</div>
    <p class="body" style="position:absolute;left:16px;top:64px;width:202px">Take a 30 min sightseeing flight from Healy airport to the heart of the mountainous Alaska Range. PHC is nestled at the base of Mt. Anderson and directly on the Pine Creek.</p>
    <div class="thumb" role="img" aria-label="Cabin in a meadow with mountains behind" style="left:17px;top:120px;width:98px;height:82px;background:linear-gradient(180deg,#b9c9d2,#5d7a45)"></div>
    <div class="thumb" role="img" aria-label="Dark log building with a peaked roof" style="left:119px;top:120px;width:98px;height:82px;background:linear-gradient(180deg,#d4dde2,#3e3029)"></div>
    <div class="thumb" role="img" aria-label="Cabin exterior wall with a window" style="left:17px;top:206px;width:98px;height:82px;background:linear-gradient(180deg,#6e4a34,#3a2a20)"></div>
    <div class="thumb" role="img" aria-label="Cabin interior with a wooden door" style="left:119px;top:206px;width:98px;height:82px;background:linear-gradient(180deg,#7a5838,#2c2630)"></div>
    <p class="body" style="position:absolute;left:16px;top:298px;width:202px">Enjoy your private cabin with access to the Main Lodge, Dining Hall, and Lounge. Tour the many rustic buildings on the premises including sauna building, theater building, old trappers cabin, and much more. 9 hiking trails lead to 2 lakes with a provided canoe.</p>
    <div class="photo" role="img" aria-label="Guests gathered around a campfire in a covered fire pit" style="top:390px;height:153px;background:linear-gradient(160deg,#7d7466,#4a3d33 50%,#2a2420)"></div>
    <svg class="curve" style="top:384px" viewBox="0 0 233 40" height="40" preserveAspectRatio="none"><path d="M0 0 L233 0 L233 6 Q110 -2 0 34Z" fill="#e6eff4"/><path d="M233 6 Q110 -2 0 34" stroke="var(--navy-1)" stroke-width="4" fill="none"/></svg>
  </div>

  <!-- Right spread: lodge -->
  <div class="panel panel--lodge wood" style="left:233px;width:467px">
    <div class="photo" role="img" aria-label="Main lodge building with antlers, golden aspens and a snowy mountain" style="height:250px;background:linear-gradient(180deg,#8fa6bb,#c9ccc6 25%,#b2a545 45%,#3a2f28 75%,#50473a)"></div>
    <svg class="curve" style="top:200px" viewBox="0 0 467 60" height="60" preserveAspectRatio="none"><path d="M0 20 Q140 70 467 30 L467 60 L0 60Z" fill="var(--wood-1)"/><path d="M0 20 Q140 70 467 30" stroke="#fff" stroke-width="3" fill="none"/></svg>
    <div class="ring" role="img" aria-label="Lodge dining room interior" style="left:258px;top:164px;width:96px;height:96px;background:radial-gradient(#b07a4a,#5e3a22)"></div>
    <div class="ring" role="img" aria-label="Glass sunroom with tables and chairs" style="left:346px;top:140px;width:108px;height:108px;background:radial-gradient(#c7d3c6,#6e7a62)"></div>
    <div class="ring" role="img" aria-label="Caribou in autumn tundra" style="left:388px;top:242px;width:72px;height:72px;background:radial-gradient(#a88a5c,#4d3d2a)"></div>

    <div class="head" style="position:absolute;left:15px;top:284px;width:210px;font-size:10.5px;line-height:1.45">Pine Hollow Camp can accommodate families, large groups, prolonged stays, and custom vacation types.</div>
    <div class="script" style="position:absolute;left:15px;top:334px;font-size:12px">Private cabins and private bathrooms!</div>
    <p class="body" style="position:absolute;left:15px;top:360px;width:206px">This is truly a wilderness lodge and we invite everyone to partake in the many outdoor activities or simply relax by the firepit, converse in the lounge, or watch the Dall sheep on Mt. Anderson from the dining room.</p>
    <p class="body" style="position:absolute;left:15px;top:426px;width:206px">Start your adventure with Skyhop Tours as they show you the mountains, rivers, glaciers, and wildlife from the air.</p>
    <p class="body" style="position:absolute;left:15px;top:470px;width:206px">Once you land at Pine Hollow Camp, our friendly staff will give you a tour of the rustic buildings and trailheads, the main lodge and dining areas, and show you to your private cabins.</p>

    <div class="band" style="left:232px;top:286px;width:150px;height:19px;font-family:'Kaushan Script',cursive;text-transform:none;font-size:11px">Guests have access to:</div>
    <ul class="list" style="position:absolute;left:252px;top:312px">
      <li>Main lodge</li><li>Palace theater</li><li>Private cabins</li><li>Wood fired sauna</li><li>Trapper's cabin museum</li><li>Lodge grounds</li><li>Otter Pond canoe</li><li>And all of the surrounding public land</li>
    </ul>
    <div class="head" style="position:absolute;left:252px;top:460px;font-size:10.5px;line-height:1.45">Remote Property!!<br>There are no roads here!! You must fly!!</div>
    <div class="head" style="position:absolute;left:252px;top:494px;width:180px;text-align:center;font-size:11.5px;color:var(--orange)">Book your trip now</div>
    <div class="band" style="left:266px;top:512px;width:152px;height:19px;font-size:11px">Call us today
      <svg viewBox="0 0 12 12"><circle cx="6" cy="6" r="5.2" fill="none" stroke="#fff" stroke-width="1"/><path d="M4 3.2l1 1.2-.6.8c.3.8.9 1.4 1.6 1.7l.8-.6 1.2 1-.6 1.1c-2-.2-3.7-2-3.9-3.9z" fill="#fff"/></svg>
      907-555-0142</div>
    <div class="web" style="left:252px;width:180px;top:532px;font-size:9.5px;line-height:1">stay@pinehollowcamp.com</div>
  </div>
</section>

</body>
</html>
```